Hispanic Financial Counseling and Advocate Firm seeks business card design

Looking for a clean, professional business card design. This is a firm that specializes in providing financial education, coaching, and planning to the Hispanic community. The name of the company is Valemar, which means to prosper. We need a design that is clean, professional, and invokes trust, professionalism, but also welcoming. Our logo is a plant growing from a hand to give the messaging of of being in control of growing your financial future and security. Its part of a larger organization names Celesta Financial Group, who's logo is a tree with multi colored branches. We have the back of the card designed so we just need the front designed. the back is blue, so front needs to be a different background color, not blue.

Target Market(s)

Hispanic Community looking to better their future

Industry/Entity Type

financial services

Contact Information for Business Card

contact info: Anselmo Ibarra Jr, 951-555-0147, info@celestafinancialgroup.example. Celestafinancialgroup.example. tag line: Para un futuro mas seguro!

Requirements
Must have
• basics: logo, contact info.
Nice to have
• possibly incorporate the tree logo provided somehow
Should not have
• should not look like the back, needs to be different from the back provided.

```html
<!DOCTYPE html>
<html lang="es">
<head>
<meta charset="utf-8">
<title>Valemar – Tarjetas de presentación</title>
<link rel="stylesheet" href="https://fonts.googleapis.com/css2?family=Montserrat:wght@400;500;600;700&display=swap">
<style>
  :root {
    --page: #e6e7e9;
    --navy: #0b3044;
    --slate: #4a5877;
    --green: #6ab23e;
    --green-soft: #dcefcf;
    --white: #ffffff;
    --leaf-green: #8cc63f;
    --leaf-blue: #2aa7df;
    --leaf-purple: #a07cc5;
    --leaf-red: #ec4a4f;
    --leaf-yellow: #f5c21b;
  }
  * { margin: 0; padding: 0; box-sizing: border-box; }
  html, body { width: 1200px; height: 852px; overflow: hidden; background: var(--page); }
  body { font-family: "Montserrat", sans-serif; position: relative; }

  .card {
    position: absolute; left: 280px; width: 640px; height: 366px;
    border-radius: 22px; overflow: hidden;
    box-shadow: 0 6px 18px rgba(0,0,0,0.18);
  }

  /* Back card */
  .card-back { top: 40px; background: var(--navy); color: var(--white); }
  .back-brand { position: absolute; left: 70px; top: 70px; display: flex; align-items: center; gap: 36px; }
  .back-mark { width: 120px; height: 120px; border-radius: 50%; background: var(--white); opacity: 0.9; }
  .back-divider { width: 1px; height: 150px; background: var(--white); opacity: 0.8; }
  .back-name { font-weight: 600; font-size: 54px; line-height: 1; letter-spacing: -1px; }
  .back-sub { display: block; font-weight: 400; font-size: 24px; letter-spacing: 0.5px; margin-top: 8px; }
  .services {
    position: absolute; left: 0; right: 0; top: 262px; text-align: center;
    font-size: 16px; font-weight: 500; line-height: 1.5;
  }
  .services span { white-space: nowrap; margin: 0 4px; }
  .dot { display: inline-block; width: 8px; height: 8px; border-radius: 50%; margin-right: 5px; vertical-align: 1px; }
  .dot.g { background: var(--leaf-green); }
  .dot.b { background: var(--leaf-blue); }
  .dot.r { background: var(--leaf-red); }
  .dot.p { background: var(--leaf-purple); }
  .dot.y { background: var(--leaf-yellow); }

  /* Front card */
  .card-front { top: 446px; background: var(--white); }
  .front-shape { position: absolute; inset: 0; }
  .sprout-area {
    position: absolute; left: 336px; top: 12px; width: 76px; height: 52px; border-radius: 6px;
    background: linear-gradient(180deg, var(--green-soft), rgba(255,255,255,0));
  }
  .front-brand { position: absolute; left: 38px; top: 38px; }
  .front-row { display: flex; align-items: center; gap: 12px; }
  .front-mark { width: 40px; height: 40px; border-radius: 50%; background: var(--green); }
  .front-name { font-size: 46px; font-weight: 600; color: var(--green); letter-spacing: -0.5px; line-height: 1.1; }
  .front-sub { margin: 4px 0 0 52px; font-size: 11px; font-weight: 700; color: var(--white); letter-spacing: 1.5px; }
  .holder { position: absolute; left: 40px; top: 148px; font-size: 24px; font-weight: 700; color: var(--green); letter-spacing: 1px; }
  .contacts { position: absolute; left: 40px; top: 194px; list-style: none; color: var(--white); font-size: 16px; }
  .contacts li { display: flex; align-items: center; gap: 10px; height: 27px; }
  .contacts svg { width: 14px; height: 14px; fill: var(--green); flex: none; }
  .rule { position: absolute; left: 40px; top: 294px; width: 44px; height: 2px; background: var(--green); }
  .tagline { position: absolute; left: 40px; top: 304px; font-size: 16px; color: var(--white); }
  .parent-brand { position: absolute; left: 470px; top: 80px; display: flex; flex-direction: column; align-items: flex-start; gap: 10px; }
  .parent-mark { width: 22px; height: 22px; border-radius: 50%; background: var(--navy); }
  .parent-name { font-size: 22px; font-weight: 600; color: var(--navy); line-height: 1.2; }
</style>
</head>
<body>

<section class="card card-back" aria-label="Reverso de la tarjeta">
  <div class="back-brand">
    <span class="back-mark"></span>
    <span class="back-divider"></span>
    <p class="back-name">Celesta<span class="back-sub">Financial Group Inc</span></p>
  </div>
  <p class="services">
    <span><i class="dot g"></i>Inmigración</span>
    <span><i class="dot b"></i>Planificacion Financiera</span><br>
    <span><i class="dot r"></i>Seguros</span>
    <span><i class="dot p"></i>Impuestos</span>
    <span><i class="dot r"></i>Y mas</span><br>
    <span><i class="dot y"></i>Preparación de documentos</span>
  </p>
</section>

<section class="card card-front" aria-label="Frente de la tarjeta">
  <svg class="front-shape" viewBox="0 0 640 366" width="640" height="366">
    <path d="M0 0 H318 L318 64 C312 134 372 182 470 208 C566 234 594 302 566 366 H0 Z" fill="#4a5877"/>
    <path d="M326 60 C320 130 380 178 478 204 C574 230 602 300 574 366" fill="none" stroke="#6ab23e" stroke-width="8"/>
  </svg>
  <div class="sprout-area" role="img" aria-label="Ilustración de brotes verdes sobre la curva"></div>

  <div class="front-brand">
    <div class="front-row">
      <span class="front-mark"></span>
      <span class="front-name">Valemar</span>
    </div>
    <p class="front-sub">SERVICIOS FINANCIEROS</p>
  </div>

  <p class="holder">ANSELMO IBARRA JR</p>
  <ul class="contacts">
    <li><svg viewBox="0 0 24 24"><path d="M6.6 10.8a15 15 0 0 0 6.6 6.6l2.2-2.2c.3-.3.7-.4 1-.2 1.1.4 2.3.6 3.6.6.6 0 1 .4 1 1V20c0 .6-.4 1-1 1A17 17 0 0 1 3 4c0-.6.4-1 1-1h3.5c.6 0 1 .4 1 1 0 1.3.2 2.5.6 3.6.1.3 0 .7-.2 1z"/></svg>951-555-0147</li>
    <li><svg viewBox="0 0 24 24"><path d="M2 5h20v14H2z M2 5l10 8 10-8"/></svg>info@celestafinancialgroup.example</li>
    <li><svg viewBox="0 0 24 24"><circle cx="12" cy="12" r="10"/></svg>Celestafinancialgroup.example</li>
  </ul>
  <span class="rule"></span>
  <p class="tagline">Para un futuro mas seguro!</p>

  <div class="parent-brand">
    <span class="parent-mark"></span>
    <p class="parent-name">Celesta<br>Financial Group</p>
  </div>
</section>

</body>
</html>
```